Coffee bag + cups: retail packaging

Our is seeking new packaging for a new coffee shop concept. As part of this we need to design new packaging for our coffee products. For this request, we are seeking design layouts for our retail bags and a cup for to-go coffee. We are working with 3 logo versions (pending final approval).

Please reference this website to see the types of coffee bag packaging options, there's a variety of bag options. We'd like the bag to be a Gusseted Bag, size 3.625 x 9.6 x 2.3125. We want a matte laminated material, not shiny.
https://www.brellumpack.com/

BAG
We'd like to see options of a black bag, blue, and kraft paper. Reference attached example.

Below is the text for our current bags, you can use that for now. I've attached example of bags that I like. We will look to you for design thoughts.

[Front]
Logo
100% Tanzanian
12oz
Dark Roast
Ground

[Back]
Amber Ridge Farms was established in 1989 by Marcus Ellery, son of baseball legend Thomas Ellery, and his family in rural Tanzania.
Today the coffee brand is sourced exclusively from the Ellery farm and other small scale family owned farms in Tanzania and East Africa.
This international coffee initiative is designed to bring a greater share of coffee revenues to farmers through direct trade and help develop rural communities in East Africa.

Visit us at Kelvorabeans.com

[Left panel]

Brewing instructions: Lorem ipsum dolor sit amet, consectetur adipiscing elit, sed do eiusmod tempor incididunt ut labore et dolore magna aliqua.

[Right panel]

Leave blank

Cup Sleeve
[Front of sleeve]
Logo

To-go cup
[Front]
Logo

Target Market(s)

Specialty coffee lovers.

Font styles to use
Serif
Sans Serif

Colors

Designer to choose colors to be used in the design.

Requirements
Must have
• Examples of coffee bag packaging.
• Must have; logo, text, clear and elegant labeling. Simple but strong.

```html
<!DOCTYPE html>
<html lang="en">
<head>
<meta charset="utf-8">
<title>Amber Ridge – Coffee Bag Layout</title>
<link rel="stylesheet" href="https://fonts.googleapis.com/css2?family=Arimo&family=PT+Sans&display=swap">
<style>
  :root {
    --paper: #ffffff;
    --bag-blue: #1440ff;
    --gold: #e3b727;
    --label-cream: #fefee6;
    --ink: #1b1b1b;
    --rule: #b9b9a8;
    --brand-brown: #6b3a1e;
    --white: #ffffff;
  }
  html, body {
    margin: 0;
    width: 1200px;
    height: 1200px;
    overflow: hidden;
    background: var(--paper);
  }
  .canvas { position: relative; width: 1200px; height: 1200px; }
  .bag {
    position: absolute; left: 151px; top: 255px;
    width: 898px; height: 691px;
    background: var(--bag-blue);
  }
  .gold-band {
    position: absolute; left: 764px; top: 255px;
    width: 83px; height: 547px;
    background: var(--gold);
  }
  .story-panel {
    position: absolute; left: 165px; top: 435px;
    width: 226px; height: 296px;
    border: 3px solid var(--gold);
    box-sizing: content-box;
  }
  .story-text {
    position: absolute; left: 12px; top: 37px; width: 202px;
    margin: 0;
    font-family: "PT Sans", sans-serif;
    font-size: 12.5px;
    line-height: 15.6px;
    color: var(--white);
    text-align: justify;
    text-align-last: center;
    hyphens: manual;
  }
  .story-text .visit { display: block; text-align: center; }
  .brewing {
    position: absolute; left: 432px; top: 474px; width: 132px;
    margin: 0;
    font-family: "Arimo", sans-serif;
    font-size: 11px;
    line-height: 14.4px;
    color: var(--white);
    text-align: justify;
    text-align-last: center;
  }
  .front-label {
    position: absolute; left: 618px; top: 587px;
    width: 431px; height: 190px;
  }
  .front-label svg.label-shape { position: absolute; inset: 0; }
  .brand-mark {
    position: absolute; left: 15px; top: 30px; width: 90px;
    font-family: "Arimo", sans-serif;
    font-size: 21px; line-height: 24px;
    color: var(--brand-brown);
    letter-spacing: 1px;
  }
  .spec {
    position: absolute; right: 228px;
    font-family: "Arimo", sans-serif;
    font-size: 18px; line-height: 20px;
    color: var(--ink);
    padding-bottom: 4px;
    text-align: right;
    white-space: nowrap;
  }
  .spec.rule::after {
    content: "";
    position: absolute; right: 0; bottom: 0;
    width: 94px;
    border-bottom: 1px solid var(--rule);
  }
  .spec.roast { top: 13px; }
  .spec.grind { top: 49px; }
  .spec.product { top: 85px; }
  .origin {
    position: absolute; left: 15px; top: 120px; width: 188px;
    font-family: "Arimo", sans-serif;
    font-size: 17px; line-height: 20px;
    letter-spacing: 2.1px;
    color: var(--ink);
    white-space: nowrap;
  }
  .weight-bar {
    position: absolute; left: 16px; top: 144px;
    width: 130px; height: 36px;
    background: var(--gold);
  }
  .weight {
    position: absolute; left: 146px; top: 154px; width: 57px;
    font-family: "Arimo", sans-serif;
    font-size: 18px; line-height: 22px;
    color: var(--ink);
    text-align: right;
    border-bottom: 1px solid var(--rule);
    padding-bottom: 3px;
    white-space: nowrap;
  }
</style>
</head>
<body>
<main class="canvas">
  <div class="bag"></div>
  <div class="gold-band"></div>

  <section class="story-panel">
    <p class="story-text">Amber Ridge Farms was established in 1989 by Marcus Ellery, son of base&shy;ball legend Thomas Ellery, and his family in rural Tanzania. Today the coffee brand is sourced exclusively from the Ellery farm and other small scale family owned farms in Tanzania and East Africa. This interna&shy;tional coffee initiative is designed to bring a greater share of coffee reve&shy;nues to farmers through direct trade and help develop rural communities in East Africa.<span class="visit">Visit us at Kelvorabeans.com</span></p>
  </section>

  <p class="brewing">Brewing instructions: Lorem ipsum dolor sit amet,consectetur adipisc&shy;ing elit, sed do eiusmod tempor incididunt ut labore et dolore magna aliqua.</p>

  <section class="front-label">
    <svg class="label-shape" width="431" height="190" viewBox="0 0 431 190" aria-hidden="true">
      <polygon fill="var(--label-cream)" points="8,0 431,0 431,190 8,190 8,186 2,182 8,178 2,174 8,170 2,166 8,162 2,158 8,154 2,150 8,146 2,142 8,138 2,134 8,130 2,126 8,122 2,118 8,114 2,110 8,106 2,102 8,98 2,94 8,90 2,86 8,82 2,78 8,74 2,70 8,66 2,62 8,58 2,54 8,50 2,46 8,42 2,38 8,34 2,30 8,26 2,22 8,18 2,14 8,10 2,6 8,2"/>
    </svg>
    <div class="brand-mark">AMBER<br>RIDGE</div>
    <div class="spec rule roast">DARK ROAST</div>
    <div class="spec rule grind">GROUND</div>
    <div class="spec rule product">COFFEE</div>
    <div class="origin">100% TANZANIAN</div>
    <div class="weight-bar"></div>
    <div class="weight">12oz</div>
  </section>
</main>
</body>
</html>
```